Owner
Vireltex Golf Cart Cushion Covers
Bright & Fun-filled
Maelys Brant
348 Heron Mill Lane
Stamford, CT
maelysbrant@snugwraps.example
snugwraps.example
Snug Wraps are golf cart cushion covers made out of Vireltex Fleece. They are made in the USA.
Vireltex fleece golf cart cushion covers
available with custom embroidery

```html
<!DOCTYPE html>
<html lang="en">
<head>
<meta charset="utf-8">
<title>Snug Wraps – Business Cards</title>
<link href="https://fonts.googleapis.com/css2?family=Source+Sans+3:wght@400;600;700&display=swap" rel="stylesheet">
<style>
  :root {
    --canvas: #ffffff;
    --card-border: #9a9a9a;
    --ink: #222222;
    --ink-light: #ffffff;
    --black: #000000;
    --magenta: #d21fc4;
    --wave-blue: #1a7fd1;
    --wave-cyan: #27c3e8;
    --wave-purple: #7b2fc1;
    --wave-green: #6fc52b;
    --wave-yellow: #f2d21b;
    --wave-red: #e8322c;
    --brand: #7b2fc1;
  }
  * { box-sizing: border-box; margin: 0; padding: 0; }
  html, body {
    width: 1200px; height: 778px; overflow: hidden;
    background: var(--canvas);
    font-family: "Source Sans 3", "Myriad Pro", sans-serif;
  }
  .sheet { position: relative; width: 1200px; height: 778px; }
  .card {
    position: absolute; overflow: hidden;
    border: 1px solid var(--card-border);
  }
  .card--front { left: 329px; top: 50px; width: 561px; height: 329px; background: #fff; }
  .card--back-light { left: 34px; top: 391px; width: 566px; height: 322px; background: #fff; }
  .card--back-dark { left: 614px; top: 391px; width: 562px; height: 322px; background: var(--black); border-color: var(--black); }

  .wave-band { position: absolute; left: 0; top: 0; width: 100%; height: 100%; }

  .heart-decor {
    position: absolute; left: 380px; top: 40px; width: 170px; height: 150px;
    border-radius: 50% 50% 45% 45%;
    background: radial-gradient(ellipse at 35% 40%, rgba(160,200,240,0.35), rgba(240,170,190,0.25) 55%, rgba(255,255,255,0) 75%);
  }

  .brand {
    position: absolute; display: flex; align-items: center; gap: 10px;
  }
  .brand__dot {
    width: 34px; height: 34px; border-radius: 50%; background: var(--brand);
  }
  .brand__name {
    font-weight: 700; font-size: 30px; line-height: 1; color: var(--brand);
    letter-spacing: 0.5px;
  }
  .card--front .brand { left: 26px; top: 52px; }
  .card--back-light .brand,
  .card--back-dark .brand { left: 50%; top: 128px; transform: translateX(-50%); }
  .card--back-dark .brand__name { color: var(--ink-light); }

  .holder-name {
    position: absolute; left: 367px; top: 180px;
    font-size: 21px; font-weight: 400; color: var(--magenta);
  }
  .contact {
    position: absolute; left: 14px; top: 250px;
    font-size: 12.5px; line-height: 18px; color: var(--ink-light);
  }
  .tagline {
    position: absolute; left: 0; right: 0; top: 255px;
    text-align: center; font-size: 15px; line-height: 19px; color: var(--ink);
  }
  .card--back-dark .tagline { color: var(--ink-light); }
</style>
</head>
<body>
<main class="sheet">

  <section class="card card--front">
    <div class="heart-decor" role="img" aria-label="Faint pastel ribbon heart decoration"></div>
    <svg class="wave-band" viewBox="0 0 561 329" aria-hidden="true">
      <path d="M0 172 C150 150 300 190 561 222 L561 232 C300 200 150 160 0 182 Z" fill="var(--wave-cyan)"/>
      <path d="M0 182 C150 160 300 200 561 232 L561 240 C300 208 150 168 0 190 Z" fill="var(--wave-blue)"/>
      <path d="M0 190 C150 168 300 208 561 240 L561 248 C300 216 150 176 0 198 Z" fill="var(--wave-purple)"/>
      <path d="M0 198 C150 176 300 216 561 248 L561 255 C300 224 150 184 0 205 Z" fill="var(--wave-green)"/>
      <path d="M0 205 C150 184 300 224 561 255 L561 261 C300 231 150 191 0 211 Z" fill="var(--wave-yellow)"/>
      <path d="M0 211 C150 191 300 231 561 261 L561 265 C300 236 150 196 0 215 Z" fill="var(--wave-red)"/>
      <path d="M0 215 C150 196 300 236 561 265 L561 329 L0 329 Z" fill="var(--black)"/>
    </svg>
    <div class="brand">
      <span class="brand__dot"></span>
      <span class="brand__name">Snug Wraps</span>
    </div>
    <p class="holder-name">Maelys Brant</p>
    <address class="contact" style="font-style:normal">
      348 Heron Mill Lane, Stamford, CT, 06902<br>
      Cell: 970-555-0148<br>
      Email: maelysbrant@snugwraps.example | www.snugwraps.example
    </address>
  </section>

  <section class="card card--back-light">
    <div class="brand">
      <span class="brand__dot"></span>
      <span class="brand__name">Snug Wraps</span>
    </div>
    <p class="tagline">Vireltex fleece golf cart cushion covers<br>available with custom embroidery</p>
  </section>

  <section class="card card--back-dark">
    <div class="brand">
      <span class="brand__dot"></span>
      <span class="brand__name">Snug Wraps</span>
    </div>
    <p class="tagline">Vireltex fleece golf cart cushion covers<br>available with custom embroidery</p>
  </section>

</main>
</body>
</html>
```